Design our branded business card!

We'd love for you to design our business card and come up with a fitting design that reflects the Pivex brand. We're a growing tech startup with big ambitions. We've included our brand guidelines (contain colour palette), logo (EPS vector in CMYK) and old designs to help you on your way.

We'd like to keep the design fairly simple:

* Name
* Phone number
* Email address
* Website (www.pivex.life)
* Twitter (@pivex)
* Address (18 Wexham Row, Leeds, UK, LS9 4ZQ).

This would need to include print and cutting marks.

If you have any questions just let us know!

Target Market(s)

Businesses, Press and our customers!

Industry/Entity Type

Business

Contact Information for Business Card

* Name
* Phone number
* Email address
* Twitter (@pivex)

Font styles to use
Sans Serif

Requirements
Must have
• 1. Must have the Pivex logo included.
• 2. Must use the font 'Brandon Text' in either 'light' or 'thin' (https://www.typevault-demo.com/fonts/qrsfonts/halden-sans/)
• 3. Must use exact colours references from the brand guidelines. Colours outside of the brand guidelines will be discounted. White (transparent) backgrounds are fine.
• 4. Must contain the following information:
• * Name
• * Phone number
• * Email address
• * Website (www.pivex.life)
• * Twitter (@pivex)
• * Address (18 Wexham Row, Leeds, UK, LS9 4ZQ).
Nice to have
• Must use the font 'Brandon Text' in either 'light' or 'thin' (https://www.typevault-demo.com/fonts/qrsfonts/halden-sans/)
Should not have
• Colours outside of the brand guidelines will be discounted. White (transparent) backgrounds are fine.
• Avoid creating icons or including photography.

```html
<!DOCTYPE html>
<html lang="en">
<head>
<meta charset="utf-8">
<title>Pivex business card</title>
<link href="https://fonts.googleapis.com/css2?family=Josefin+Sans:wght@300;400&display=swap" rel="stylesheet">
<style>
  :root {
    --page-bg: #ececec;
    --card-white: #ffffff;
    --brand-green: #9dc97e;
    --ink-grey: #5a5a5a;
    --label-box: #4a4a4a;
    --text-white: #ffffff;
  }
  * { box-sizing: border-box; margin: 0; padding: 0; }
  html, body {
    width: 1200px; height: 687px; overflow: hidden;
    background: var(--page-bg);
    font-family: "Josefin Sans", "Helvetica Neue", Arial, sans-serif;
    font-weight: 300;
  }
  .sheet {
    position: relative; width: 1200px; height: 687px;
    display: flex; align-items: center; justify-content: center; gap: 70px;
  }
  .card {
    position: relative; width: 500px; height: 310px;
    box-shadow: 0 10px 30px rgba(0,0,0,0.12);
  }

  /* Front */
  .card-front { background: var(--card-white); }
  .front-brand {
    position: absolute; left: 56px; top: 78px;
    display: flex; align-items: center; gap: 18px;
  }
  .brand-dot {
    width: 84px; height: 84px; border-radius: 50%;
    background: var(--brand-green);
  }
  .front-wordmark {
    font-size: 92px; line-height: 1; color: var(--ink-grey);
    font-weight: 300; letter-spacing: 1px; padding-top: 14px;
  }
  .front-tagline {
    position: absolute; left: 56px; right: 40px; top: 214px;
    font-size: 15px; letter-spacing: 3.2px; color: var(--ink-grey);
  }
  .front-url {
    position: absolute; left: 112px; top: 240px;
    font-size: 15px; letter-spacing: 3px; color: var(--brand-green);
  }

  /* Back */
  .card-back { background: var(--brand-green); color: var(--text-white); }
  .holder-name {
    position: absolute; left: 36px; top: 168px;
    font-size: 34px; letter-spacing: 1.5px; font-weight: 300;
  }
  .holder-rule {
    position: absolute; left: 36px; top: 214px; width: 190px; height: 1px;
    background: var(--text-white);
  }
  .back-brand {
    position: absolute; left: 36px; top: 230px;
    display: flex; align-items: center; gap: 8px;
  }
  .back-brand .brand-dot {
    width: 30px; height: 30px; background: var(--text-white);
  }
  .back-wordmark { font-size: 32px; line-height: 1; padding-top: 6px; }

  .contact-list {
    position: absolute; left: 250px; top: 46px; width: 230px;
    display: flex; flex-direction: column; gap: 6px;
    font-size: 14px;
  }
  .contact-row { display: flex; align-items: flex-start; gap: 6px; }
  .contact-label { white-space: nowrap; padding-top: 3px; }
  .contact-value {
    background: var(--label-box); color: var(--text-white);
    padding: 3px 5px 1px; line-height: 1.25; font-size: 14px;
  }
  .contact-divider {
    height: 1px; background: var(--text-white); margin: 8px 0 6px;
  }
</style>
</head>
<body>
<main class="sheet">
  <section class="card card-front" aria-label="Card front">
    <div class="front-brand">
      <span class="brand-dot"></span>
      <span class="front-wordmark">pivex</span>
    </div>
    <p class="front-tagline">The World's Smartest Home Security</p>
    <p class="front-url">www.pivex.life</p>
  </section>

  <section class="card card-back" aria-label="Card back">
    <h1 class="holder-name">JOHN DOE</h1>
    <div class="holder-rule"></div>
    <div class="back-brand">
      <span class="brand-dot"></span>
      <span class="back-wordmark">pivex</span>
    </div>

    <div class="contact-list">
      <div class="contact-row"><span class="contact-label">Phone numbers</span><span class="contact-value">001 555 0192</span></div>
      <div class="contact-row"><span class="contact-label">Email</span><span class="contact-value">johndoe@pivex.com</span></div>
      <div class="contact-divider"></div>
      <div class="contact-row"><span class="contact-label">Website</span><span class="contact-value">www.pivex.life</span></div>
      <div class="contact-row"><span class="contact-label">Twitter</span><span class="contact-value">@pivex</span></div>
      <div class="contact-row"><span class="contact-label">Address</span><span class="contact-value">18 Wexham Row, Leeds,<br>UK, LS9 4ZQ</span></div>
    </div>
  </section>
</main>
</body>
</html>
```